Business Card Design

We would like a business card that utilizes our current logo and keeps with the same feel - elegant and organic. Our farm isn't about mass production, it's about excellence, education, beautiful events and flowers - people, culture, and community.

Target Market(s)

Patrons to our farm who are interested in weddings, events, or our flowers and vegetables.

Contact Information for Business Card

Name, address, cell email (Danielle Hoskins, 2716 Wrenfield Rd, Longmont, CO 80503, cell 30.412.6638, email danielle@wrenfieldacres.com)

```html
<!DOCTYPE html>
<html lang="en">
<head>
<meta charset="utf-8">
<title>Wrenfield Acres – Business Card</title>
<link href="https://fonts.googleapis.com/css2?family=Montserrat:wght@400;600&display=swap" rel="stylesheet">
<style>
  :root {
    --backdrop: #2a2a2a;
    --card-white: #f7f7f5;
    --sage: #6b8470;
    --sage-light: #7f9883;
    --sage-text: #647c68;
    --ink: #2b2b2b;
    --cream: #f4f1ea;
  }
  * { margin: 0; padding: 0; box-sizing: border-box; }
  html, body { width: 1200px; height: 900px; overflow: hidden; }
  body {
    background: var(--backdrop);
    font-family: "Montserrat", sans-serif;
    display: flex;
    align-items: center;
    justify-content: center;
    gap: 70px;
  }
  .card {
    width: 360px;
    height: 620px;
    border-radius: 30px;
    position: relative;
    overflow: hidden;
  }
  .card-front {
    background: linear-gradient(160deg, #ffffff 0%, var(--card-white) 60%, #ececea 100%);
    display: flex;
    flex-direction: column;
    align-items: center;
    color: var(--ink);
    text-align: center;
  }
  .brand-name {
    margin-top: 120px;
    font-weight: 400;
    font-size: 34px;
    letter-spacing: 1px;
    color: var(--sage-text);
  }
  .contact-person { margin-top: 150px; }
  .person-name {
    font-weight: 600;
    font-size: 24px;
    color: var(--sage-text);
  }
  .person-title {
    font-size: 14px;
    margin-top: 2px;
  }
  .icon-divider {
    display: flex;
    align-items: center;
    gap: 10px;
    margin-top: 26px;
  }
  .rule {
    width: 56px;
    height: 1.5px;
    background: var(--sage-text);
  }
  .rule-long { width: 60px; }
  .icon-row { display: flex; gap: 3px; }
  .contact-lines {
    margin-top: 18px;
    font-size: 15px;
    line-height: 1.75;
  }
  .short-rule {
    width: 44px;
    height: 1.5px;
    background: var(--sage-text);
    margin: 18px auto;
  }
  .address {
    font-size: 15px;
    line-height: 1.35;
  }
  .card-back {
    background: linear-gradient(200deg, var(--sage) 0%, var(--sage-light) 100%);
  }
  .back-brand {
    position: absolute;
    left: 50%;
    top: 50%;
    transform: translate(-50%, -50%) rotate(-90deg);
    white-space: nowrap;
    font-weight: 400;
    font-size: 50px;
    letter-spacing: 2px;
    color: var(--cream);
  }
</style>
</head>
<body>
  <section class="card card-front">
    <div class="brand-name">Wrenfield Acres</div>

    <div class="contact-person">
      <div class="person-name">Danielle Hoskins</div>
      <div class="person-title">Owner</div>
    </div>

    <div class="icon-divider">
      <span class="rule"></span>
      <svg class="icon-row" width="78" height="22" viewBox="0 0 78 22" aria-hidden="true">
        <g fill="#647c68">
          <rect x="0" y="0" width="24" height="22" rx="4"/>
          <rect x="27" y="0" width="24" height="22" rx="4"/>
          <rect x="54" y="0" width="24" height="22" rx="4"/>
        </g>
        <g fill="none" stroke="#ffffff" stroke-width="1.6" stroke-linecap="round" stroke-linejoin="round">
          <path d="M8 6 q-1 5 4 10 q2 1 4 0 l0-2 l-3-1 l-1 1 q-3-2-4-5 l1-1 l-1-3 z"/>
          <rect x="32" y="6" width="14" height="10" rx="1"/>
          <path d="M32 7 l7 5 l7-5"/>
          <circle cx="66" cy="11" r="6"/>
          <path d="M60 11 h12 M66 5 q-3 6 0 12 q3-6 0-12"/>
        </g>
      </svg>
      <span class="rule rule-long"></span>
    </div>

    <div class="contact-lines">
      <div>30.412.6638</div>
      <div>danielle@wrenfieldacres.com</div>
      <div>www.wrenfieldacres.com</div>
    </div>

    <div class="short-rule"></div>

    <div class="address">
      <div>2716 Wrenfield Rd</div>
      <div>Longmont, CO 80503</div>
    </div>
  </section>

  <section class="card card-back">
    <div class="back-brand">Wrenfield Acres</div>
  </section>
</body>
</html>
```